Oven Cleaning Business owner needs business card design

Hi there,
Would like for a business card to be designed for myself, the owner of a professional oven cleaning business on the Sunshine Coast.
Would like it to look sleek, and modern-ish. Bit creative is encouraged too.
Include following:
Name/title: Corin de Walbrek, Owner
Phone number: 1300 482 906
Email: info@kitchenlustrely.com.au
Website: www.kitchenlustrely.com.au

```html
<!DOCTYPE html>
<html lang="en">
<head>
<meta charset="utf-8">
<title>Kitchen Lustrely — Business Card</title>
<link rel="stylesheet" href="https://fonts.googleapis.com/css2?family=Arimo:wght@400;700&display=swap">
<style>
  :root {
    --page-bg: #b9b9b9;
    --card-white: #ffffff;
    --brand-teal: #4ec3cc;
    --pattern-teal: #3fa9b2;
    --ink-dark: #1f2326;
    --ink-mid: #2b2f33;
    --divider: #555a5e;
  }
  * { box-sizing: border-box; margin: 0; padding: 0; }
  html, body {
    width: 1200px; height: 802px; overflow: hidden;
    background: var(--page-bg);
    font-family: "Arimo", Arial, sans-serif;
  }
  .canvas {
    position: relative; width: 1200px; height: 802px;
    display: flex; align-items: center; justify-content: center; gap: 60px;
  }
  .card {
    position: relative; width: 520px; height: 298px;
    border-radius: 20px; overflow: hidden;
    box-shadow: 0 10px 28px rgba(0,0,0,0.22);
  }
  /* Front */
  .card--front { background: var(--card-white); }
  .brand {
    position: absolute; left: 42px; top: 50%; transform: translateY(-50%);
    display: flex; align-items: center; gap: 12px;
  }
  .brand__dot {
    width: 34px; height: 34px; border-radius: 50%;
    background: var(--brand-teal); flex: none;
  }
  .brand__name {
    font-weight: 700; font-size: 25px; line-height: 1.05;
    letter-spacing: 0.5px; color: var(--ink-dark); text-transform: uppercase;
  }
  .divider {
    position: absolute; left: 258px; top: 92px; width: 1px; height: 114px;
    background: var(--divider);
  }
  .contact {
    position: absolute; left: 280px; top: 80px;
  }
  .contact__name {
    font-weight: 700; font-size: 21px; color: var(--brand-teal); line-height: 1.1;
  }
  .contact__title {
    font-size: 14px; color: var(--ink-mid); margin-top: 2px;
  }
  .contact__list { list-style: none; margin-top: 16px; }
  .contact__item {
    display: flex; align-items: center; gap: 7px;
    font-size: 12.5px; color: var(--ink-mid); line-height: 1.75;
  }
  .contact__icon { width: 11px; height: 11px; flex: none; }
  /* Back */
  .card--back { background: var(--brand-teal); }
  .back__pattern {
    position: absolute; inset: 0;
    background: linear-gradient(135deg, var(--brand-teal), var(--pattern-teal));
    opacity: 0.55;
  }
  .back__brand {
    position: absolute; right: 44px; top: 50%; transform: translateY(-50%);
    display: flex; align-items: center; gap: 12px;
  }
  .back__dot {
    width: 34px; height: 34px; border-radius: 50%;
    background: var(--card-white); flex: none;
  }
  .back__name {
    font-weight: 700; font-size: 25px; line-height: 1.05;
    letter-spacing: 0.5px; color: var(--card-white); text-transform: uppercase;
  }
</style>
</head>
<body>
<main class="canvas">
  <section class="card card--front" aria-label="Card front">
    <div class="brand">
      <span class="brand__dot"></span>
      <span class="brand__name">Kitchen<br>Lustrely</span>
    </div>
    <div class="divider"></div>
    <div class="contact">
      <p class="contact__name">Corin de Walbrek</p>
      <p class="contact__title">Owner</p>
      <ul class="contact__list">
        <li class="contact__item">
          <svg class="contact__icon" viewBox="0 0 24 24" fill="var(--brand-teal)"><path d="M6.6 10.8a15.1 15.1 0 0 0 6.6 6.6l2.2-2.2a1 1 0 0 1 1-.25 11.4 11.4 0 0 0 3.6.57 1 1 0 0 1 1 1V20a1 1 0 0 1-1 1A17 17 0 0 1 3 4a1 1 0 0 1 1-1h3.5a1 1 0 0 1 1 1c0 1.25.2 2.45.57 3.57a1 1 0 0 1-.25 1z"/></svg>
          1300 482 906
        </li>
        <li class="contact__item">
          <svg class="contact__icon" viewBox="0 0 24 24" fill="var(--brand-teal)"><path d="M2 5h20v14H2z"/><path d="M2 5l10 8 10-8" fill="none" stroke="#fff" stroke-width="2"/></svg>
          info@kitchenlustrely.com.au
        </li>
        <li class="contact__item">
          <svg class="contact__icon" viewBox="0 0 24 24" fill="none" stroke="var(--brand-teal)" stroke-width="2.2"><circle cx="12" cy="12" r="10"/><path d="M2 12h20M12 2c3 3 3 17 0 20M12 2c-3 3-3 17 0 20"/></svg>
          www.kitchenlustrely.com.au
        </li>
      </ul>
    </div>
  </section>

  <section class="card card--back" aria-label="Card back">
    <div class="back__pattern" role="img" aria-label="Repeating pattern of faint brand marks across the teal background"></div>
    <div class="back__brand">
      <span class="back__dot"></span>
      <span class="back__name">Kitchen<br>Lustrely</span>
    </div>
  </section>
</main>
</body>
</html>
```